KTNW Unique Letterhead for Financial Services Business

I am looking for a letterhead design to match our branding colours. I do not want to see anything generic that could be created in word, I can do that myself, I am after something with a bit of designer flair. Once completed I will need files in a print ready format (including bleed area).

I have included our logo file and also our new business card design but get creative.

Industry/Entity Type

Financial Services

Font styles to use
Other font styles liked:
• raleway

Colors
00AB8E
00BBA5
67D7C9
C6EFE9
E9F9F6

Requirements
Must have
• Must be consisten with logo branding colours.
Should not have
• Anything generic that I could create myself in word

```html
<!DOCTYPE html>
<html lang="en">
<head>
<meta charset="utf-8">
<title>KTNW Financial Services – Letterhead</title>
<link href="https://fonts.googleapis.com/css2?family=Raleway:wght@400;700&family=Source+Sans+3:wght@400&display=swap" rel="stylesheet">
<style>
  :root {
    --teal: #00868f;
    --teal-bright: #14a99d;
    --teal-deep: #05596d;
    --text-grey: #9b9b9b;
    --paper: #ffffff;
  }
  html, body { margin: 0; padding: 0; overflow: hidden; }
  body { width: 960px; height: 1200px; background: var(--paper); }
  .letterhead { position: relative; width: 960px; height: 1200px; overflow: hidden; background: var(--paper); }

  .brand {
    position: absolute; top: 114px; left: 0; width: 960px;
    display: flex; justify-content: center; align-items: center; gap: 12px;
  }
  .brand-mark { width: 22px; height: 22px; background: var(--teal); }
  .brand-name {
    font-family: "Raleway", sans-serif; font-weight: 400;
    font-size: 30px; letter-spacing: 1px; color: var(--teal);
  }

  .salutation {
    position: absolute; top: 307px; left: 82px;
    font-family: "Source Sans 3", sans-serif; font-size: 17.6px; color: var(--text-grey);
  }
  .body-copy {
    position: absolute; top: 383px; left: 61px; width: 838px;
    font-family: "Source Sans 3", sans-serif; font-size: 17.6px; line-height: 21.8px;
    color: var(--text-grey); text-align: justify;
  }
  .body-copy p { margin: 0 0 22px; }
  .body-copy p:first-child { text-indent: 56px; }

  .footer-band { position: absolute; left: 0; top: 0; width: 960px; height: 1200px; }

  .contact {
    position: absolute; left: 586px; top: 1106px; list-style: none; margin: 0; padding: 0;
    font-family: "Raleway", sans-serif; font-weight: 700; font-size: 14.4px; color: #fff;
  }
  .contact li { display: flex; align-items: center; gap: 10px; height: 18px; }
  .contact li.gap { margin-top: 5px; }
  .contact svg { width: 14px; height: 14px; flex: none; }
</style>
</head>
<body>
<div class="letterhead">
  <div class="brand">
    <span class="brand-mark"></span>
    <span class="brand-name">KTNW FINANCIAL SERVICES</span>
  </div>

  <div class="salutation">Dear Sir</div>

  <div class="body-copy">
    <p>Lorem ipsum dolor sit amet, consectetur adipiscing elit. Integer eu odio mattis, pulvinar turpis quis, faucibus nisl. Proin feugiat, erat vitae cursus pharetra, enim est semper ligula, in malesuada orci nisl et diam. Etiam elementum metus ac fringilla vulputate. Etiam mattis ligula sed ante mollis bibendum. Orci varius natoque penatibus et magnis dis parturient montes, nascetur ridiculus mus.</p>
    <p>Ut nibh augue, blandit ac orci ac, rutrum congue enim. Suspendisse gravida vulputate felis, quis interdum orci tincidunt quis. Praesent imperdiet maximus neque. Mauris ut dui enim. Nullam at efficitur elit. Donec ante ipsum, fermentum at lectus vel, blandit vulputate ante. Proin luctus suscipit diam id vestibulum. Morbi malesuada id mauris eget ullamcorper.</p>
    <p>Donec varius orci purus, vitae aliquam libero volutpat id. Integer sed imperdiet libero. Aliquam accumsan, risus sit amet ornare consectetur, turpis felis dictum justo, non rhoncus mauris dui sed velit. Pellentesque habitant morbi tristique senectus et netus et malesuada fames ac turpis egestas. Pellentesque tincidunt vitae ligula nec imperdiet. Donec sed congue enim. Nullam elementum faucibus nulla nec vestibulum. Sed at tempor ligula. In quis vulputate nunc. Integer at gravida lacus, ac tristique risus. Sed at vulputate nulla.</p>
    <p>Praesent blandit nunc eu efficitur commodo. In tempor nisi ex, vel venenatis ante vestibulum a. Duis vestibulum nibh a erat sagittis, nec euismod lorem varius. Nam ultricies turpis sed justo sollicitudin volutpat. Morbi sed mollis eros. Sed quis tortor id enim vehicula porttitor. Curabitur non aliquam ex. Phasellus dignissim fermentum elit, at finibus ligula mattis eget.</p>
  </div>

  <svg class="footer-band" viewBox="0 0 960 1200" role="img" aria-label="Decorative footer band in brand teal tones">
    <defs>
      <linearGradient id="footer-fill" x1="0" y1="0" x2="1" y2="0">
        <stop offset="0" stop-color="#05596d"/>
        <stop offset="1" stop-color="#14a99d"/>
      </linearGradient>
    </defs>
    <polygon points="0,1060 960,990 960,1200 0,1200" fill="url(#footer-fill)"/>
  </svg>

  <ul class="contact">
    <li>
      <svg viewBox="0 0 14 14"><path d="M7 1a4 4 0 0 0-4 4c0 3 4 8 4 8s4-5 4-8a4 4 0 0 0-4-4zm0 5.5A1.5 1.5 0 1 1 7 3.5a1.5 1.5 0 0 1 0 3z" fill="#fff"/></svg>
      PO Box 4187 Ridgeview NSW 2390
    </li>
    <li>
      <svg viewBox="0 0 14 14"><path d="M3 1.5l2 .2 1 2.8-1.4 1a7 7 0 0 0 3.9 3.9l1-1.4 2.8 1 .2 2c-.2.6-.8 1-1.5 1C5.5 12 2 8.5 2 3c0-.7.4-1.3 1-1.5z" fill="#fff"/></svg>
      0400 555 218
    </li>
    <li class="gap">
      <svg viewBox="0 0 14 14"><rect x="1" y="4" width="12" height="8" rx="1" fill="#fff"/><path d="M1.5 4.5L7 8.5l5.5-4" stroke="#0d8f92" stroke-width="1.2" fill="none"/></svg>
      info@ktnwfinancial.com.au
    </li>
    <li>
      <svg viewBox="0 0 14 14" fill="none" stroke="#fff" stroke-width="1.1"><circle cx="7" cy="7" r="5.5"/><ellipse cx="7" cy="7" rx="2.4" ry="5.5"/><path d="M1.5 7h11M2.3 4.2h9.4M2.3 9.8h9.4"/></svg>
      www.ktnwfinancial.com.au
    </li>
  </ul>
</div>
</body>
</html>
```